Steadfast Care - Need Stationary Design

We need a stationary pack for our new Care company based in the uk
Are corporate colours are Pink and purple
Please use attached logo
Target Market(s)
The Care Industry
Industry/Entity Type
It Company
Contact Information for Business Card
Melissa Rowden
Director

```html
<!DOCTYPE html>
<html lang="en">
<head>
<meta charset="utf-8">
<title>Steadfast Care – Stationery</title>
<link rel="stylesheet" href="https://fonts.googleapis.com/css2?family=Didact+Gothic&display=swap">
<style>
:root{
  --bg:#ececec;
  --paper:#ffffff;
  --purple:#7a559f;
  --pink:#d4307f;
  --lilac:#b59bd0;
  --lilac-soft:#e8def2;
  --ink:#3d3450;
  --rule:#9a80bb;
}
*{box-sizing:border-box;margin:0;padding:0}
html,body{width:1200px;height:1200px;overflow:hidden}
body{background:var(--bg);font-family:"Didact Gothic",sans-serif;color:var(--ink);position:relative}
.sheet{position:absolute;background:var(--paper);box-shadow:0 2px 8px rgba(0,0,0,.12);overflow:hidden}

/* wordmark */
.wordmark{display:flex;align-items:center;gap:8px;color:var(--purple);font-weight:400;white-space:nowrap;line-height:1}
.wordmark .dot{width:.7em;height:.7em;border-radius:50%;background:var(--pink);flex:none}

/* faint decoration stand-in */
.decor{position:absolute;border-radius:50%;background:radial-gradient(circle,rgba(255,255,255,.38),rgba(255,255,255,0) 70%)}

/* icons */
.ico{width:11px;height:11px;flex:none}

/* shared contact blocks */
.contact-list{position:absolute;list-style:none;text-align:right;white-space:nowrap}
.contact-list li{display:flex;justify-content:flex-end;align-items:center;gap:6px}
.address{position:absolute;display:flex;align-items:center;gap:6px;border-top:1px solid var(--rule);white-space:nowrap}

/* letterhead */
.letterhead{left:50px;top:204px;width:560px;height:792px;
  background:linear-gradient(172deg,var(--paper) 45%,var(--lilac-soft) 70%,var(--lilac) 100%)}
.letterhead .wordmark{position:absolute;left:36px;top:48px;font-size:26px}
.letterhead .decor{left:-40px;bottom:-60px;width:320px;height:320px}
.letterhead .contact-list{right:24px;bottom:78px;font-size:13px;line-height:1.8}
.letterhead .address{right:24px;bottom:26px;width:300px;justify-content:flex-end;font-size:13px;padding-top:9px}

/* envelope front */
.envelope-front{left:650px;top:204px;width:500px;height:240px;
  background:linear-gradient(160deg,var(--paper) 40%,var(--lilac-soft) 65%,var(--lilac) 100%)}
.envelope-front .wordmark{position:absolute;left:26px;top:40px;font-size:22px}
.envelope-front .decor{right:-20px;bottom:-80px;width:260px;height:260px}
.envelope-front .address{left:12px;bottom:14px;width:230px;font-size:11px;padding-top:7px}

/* envelope back */
.envelope-back{left:650px;top:474px;width:500px;height:240px}
.envelope-back .flap{position:absolute;inset:0;width:100%;height:100%}

/* business cards */
.card{width:240px;height:150px;border-radius:12px;top:754px}
.card-front{left:650px;background:linear-gradient(125deg,var(--paper) 20%,var(--lilac-soft) 60%,var(--lilac) 100%);
  display:flex;align-items:center;justify-content:center}
.card-front .wordmark{font-size:18px}
.card-front .decor{right:-10px;bottom:-40px;width:150px;height:150px}
.card-back{left:910px;background:linear-gradient(115deg,var(--lilac) 0%,var(--lilac-soft) 35%,var(--paper) 70%)}
.card-back .wordmark{position:absolute;left:14px;top:18px;font-size:12px;gap:6px}
.card-back .decor{left:-20px;bottom:-30px;width:130px;height:130px}
.card-back .person{position:absolute;right:14px;top:38px;text-align:right}
.card-back .person-name{font-size:15px;color:var(--purple);line-height:1.1}
.card-back .person-role{font-size:8px;color:var(--ink)}
.card-back .contact-list{right:14px;top:74px;font-size:8px;line-height:1.6}
.card-back .ico{width:8px;height:8px}
.card-back .contact-list li{gap:4px}
.card-back .address{right:12px;bottom:10px;width:160px;justify-content:flex-end;font-size:8px;padding-top:5px;gap:4px}
</style>
</head>
<body>

<svg width="0" height="0" style="position:absolute">
  <defs>
    <symbol id="i-pin" viewBox="0 0 10 10"><path d="M5 0a3.5 3.5 0 0 0-3.5 3.5C1.5 6 5 10 5 10s3.5-4 3.5-6.5A3.5 3.5 0 0 0 5 0zm0 5a1.4 1.4 0 1 1 0-2.8A1.4 1.4 0 0 1 5 5z" fill="#d4307f"/></symbol>
    <symbol id="i-phone" viewBox="0 0 10 10"><rect x="2.5" y="0.5" width="5" height="9" rx="1" fill="#d4307f"/><rect x="3.5" y="1.8" width="3" height="5.5" fill="#fff"/></symbol>
    <symbol id="i-web" viewBox="0 0 10 10"><circle cx="5" cy="5" r="4.3" fill="none" stroke="#d4307f" stroke-width="1.2"/><path d="M0.7 5h8.6M5 0.7v8.6" stroke="#d4307f" stroke-width="1"/></symbol>
    <symbol id="i-mail" viewBox="0 0 10 10"><rect x="0.5" y="2" width="9" height="6" fill="#d4307f"/><path d="M0.5 2l4.5 3.5L9.5 2" fill="none" stroke="#fff" stroke-width="0.8"/></symbol>
  </defs>
</svg>

<section class="sheet letterhead" aria-label="Letterhead">
  <div class="wordmark"><span class="dot"></span>Steadfast Care</div>
  <div class="decor" role="img" aria-label="Faint brand decoration area"></div>
  <ul class="contact-list">
    <li>xxxxxxxxxx <svg class="ico"><use href="#i-phone"/></svg></li>
    <li>www.steadfastcare.example <svg class="ico"><use href="#i-web"/></svg></li>
    <li>melissa@steadfastcare.example <svg class="ico"><use href="#i-mail"/></svg></li>
  </ul>
  <p class="address">Dummy City dummy Country dummy Land <svg class="ico"><use href="#i-pin"/></svg></p>
</section>

<section class="sheet envelope-front" aria-label="Envelope front">
  <div class="wordmark"><span class="dot"></span>Steadfast Care</div>
  <div class="decor" role="img" aria-label="Faint brand decoration area"></div>
  <p class="address"><svg class="ico"><use href="#i-pin"/></svg> Dummy City dummy Country dummy Land</p>
</section>

<section class="sheet envelope-back" aria-label="Envelope back">
  <svg class="flap" viewBox="0 0 500 240" preserveAspectRatio="none">
    <defs>
      <linearGradient id="flapFill" x1="0" y1="0" x2="0" y2="1">
        <stop offset="0" stop-color="#ffffff"/>
        <stop offset="1" stop-color="#b59bd0"/>
      </linearGradient>
    </defs>
    <path d="M0 0H500C480 38 452 58 404 65C346 73 288 86 250 106C212 86 154 73 96 65C48 58 20 38 0 0Z" fill="url(#flapFill)"/>
  </svg>
</section>

<section class="sheet card card-front" aria-label="Business card front">
  <div class="decor" role="img" aria-label="Faint brand decoration area"></div>
  <div class="wordmark"><span class="dot"></span>Steadfast Care</div>
</section>

<section class="sheet card card-back" aria-label="Business card back">
  <div class="decor" role="img" aria-label="Faint brand decoration area"></div>
  <div class="wordmark"><span class="dot"></span>Steadfast Care</div>
  <div class="person">
    <p class="person-name">Melissa Rowden</p>
    <p class="person-role">Director</p>
  </div>
  <ul class="contact-list">
    <li>xxxxxxxxxx <svg class="ico"><use href="#i-phone"/></svg></li>
    <li>www.steadfastcare.example <svg class="ico"><use href="#i-web"/></svg></li>
    <li>melissa@steadfastcare.example <svg class="ico"><use href="#i-mail"/></svg></li>
  </ul>
  <p class="address">Dummy City dummy Country dummy Land <svg class="ico"><use href="#i-pin"/></svg></p>
</section>

</body>
</html>
```